Landing Page for a new, High Production, farming technology

Brightfield Sprout
We need a single landing page, with an email signup for more information.
We build self-contained, farming boxes out of ISO containers. These containers use hydroponics and LED lighting to provide a year round growing environment for crops. So, you could grow crops anywhere at any time of the year in any environment.
For the purpose of this site, we will be doing split testing between several different themes using different sites and keywords.
This site's focus should be providing our product to people searching for high production farming technology.
We'll be focusing on the following key words: Agriculture, aquaponics, farm, garden, hydroponics, organic food, subsistence farming, urban farming, vertical garden.
Target Market(s)
We are going to be using this page to judge that
Number of Pages Required
1 page
Look and feel
Each slider illustrates characteristics of the customer's brand and the style your logo design should communicate.

```html
<!DOCTYPE html>
<html lang="en">
<head>
<meta charset="utf-8">
<title>Brightfield Sprout – Year-Round Container Farming</title>
<link href="https://fonts.googleapis.com/css2?family=Montserrat:wght@400;500;700&display=swap" rel="stylesheet">
<style>
  :root {
    --backdrop: #e6e6e6;
    --page: #ffffff;
    --header-orange: #e9ab71;
    --sage: #9dba9c;
    --ink: #1f1f1f;
    --black: #000000;
    --form-grey: #f2f2f2;
    --field-grey: #d3d3d3;
    --field-text: #333333;
    --button-green: #1e2b12;
    --footer-dark: #131a0b;
    --keyword-box: rgba(20, 16, 10, 0.88);
    --white: #ffffff;
  }
  * { box-sizing: border-box; margin: 0; padding: 0; }
  html, body { width: 960px; height: 1200px; overflow: hidden; }
  body {
    position: relative;
    background: var(--backdrop);
    font-family: "Montserrat", sans-serif;
    color: var(--ink);
  }
  .page {
    position: absolute; left: 77px; top: 0;
    width: 806px; height: 1200px;
    background: var(--page);
  }
  .site-header {
    position: absolute; left: 93px; top: 0;
    width: 774px; height: 206px;
    background: var(--header-orange);
    display: flex; align-items: center; justify-content: center;
  }
  .brand-name {
    font-size: 30px; font-weight: 500;
    letter-spacing: 5px; text-transform: uppercase;
    color: #333333;
  }
  .intro {
    position: absolute; left: 93px; top: 208px;
    width: 774px; height: 215px;
    background: var(--sage);
    display: flex; align-items: center; justify-content: center;
    padding: 0 28px;
  }
  .intro p {
    font-size: 19.2px; line-height: 24px; text-align: center;
    color: var(--ink);
  }
  .signup {
    position: absolute; left: 93px; top: 423px;
    width: 775px; height: 216px;
  }
  .signup-shape { position: absolute; left: 0; top: 0; }
  .plane-art {
    position: absolute; left: 52px; top: 10px;
    width: 230px; height: 150px;
    background: #f4f4f4;
  }
  .signup-title {
    position: absolute; left: 342px; top: 4px;
    height: 58px; line-height: 58px;
    font-size: 19.2px; font-weight: 500; color: var(--white);
  }
  .field {
    position: absolute; left: 337px;
    width: 242px; height: 30px;
    background: var(--field-grey);
    font-size: 14px; color: var(--field-text);
    padding-left: 11px; line-height: 30px;
  }
  .field-name { top: 82px; }
  .field-email { top: 125px; padding-left: 10px; }
  .submit {
    position: absolute; left: 339px; top: 168px;
    width: 127px; height: 33px;
    background: var(--button-green); color: var(--white);
    font-size: 14px; font-weight: 700;
    display: flex; align-items: center; justify-content: center;
  }
  .keywords-section {
    position: absolute; left: 93px; top: 639px;
    width: 775px; height: 503px;
  }
  .keywords-photo {
    position: absolute; inset: 0;
    background:
      radial-gradient(ellipse 190px 230px at 250px 250px, #3f7a2a 0%, #4d6330 55%, rgba(80,70,50,0) 100%),
      linear-gradient(180deg, #2b3418 0%, #5e5233 40%, #7b6a4d 70%, #b59d78 100%);
  }
  .keyword-list { position: absolute; left: 517px; top: 51px; list-style: none; }
  .keyword-list li {
    width: 241px; height: 44px; margin-bottom: 4px;
    background: var(--keyword-box);
    color: var(--white);
    font-size: 19.2px; line-height: 44px;
    padding-left: 22px; letter-spacing: 0.3px;
  }
  .site-footer {
    position: absolute; left: 94px; top: 1142px;
    width: 775px; height: 58px;
    background: var(--footer-dark);
    color: var(--white);
    font-size: 13px;
    display: flex; align-items: center; justify-content: center;
  }
</style>
</head>
<body>
  <div class="page"></div>

  <header class="site-header">
    <span class="brand-name">Brightfield Sprout</span>
  </header>

  <section class="intro">
    <p>We build self-contained, farming boxes out of ISO containers.<br>
    These containers use hydroponics and LED lighting to provide a year round growing environment for crops. So, you could grow crops anywhere at any time of the year in any environment.</p>
  </section>

  <section class="signup">
    <svg class="signup-shape" width="775" height="216" viewBox="0 0 775 216">
      <polygon points="315,4 775,4 775,216 219,216" fill="#f2f2f2"/>
      <line x1="296" y1="62" x2="221" y2="216" stroke="#000" stroke-width="5"/>
      <polygon points="314,4 775,4 775,62 290,62" fill="#000"/>
    </svg>
    <div class="plane-art" role="img" aria-label="Line drawing of a paper plane with a dashed flight trail"></div>
    <h2 class="signup-title">Signup With Your Email</h2>
    <div class="field field-name">Name :</div>
    <div class="field field-email">Email :</div>
    <div class="submit">Submit</div>
  </section>

  <section class="keywords-section">
    <div class="keywords-photo" role="img" aria-label="Photo of a leafy green tree growing from a half sphere of soil on a blurred earthy background"></div>
    <ul class="keyword-list">
      <li>Agriculture</li>
      <li>Aquaponics</li>
      <li>Farm</li>
      <li>Garden</li>
      <li>Hydroponics</li>
      <li>Organic Food</li>
      <li>Subsistence Farming</li>
      <li>Urban Farming</li>
      <li>Vertical Garden</li>
    </ul>
  </section>

  <footer class="site-footer">Copyright All Rights Reserved.</footer>
</body>
</html>
```